Stationery using new logo for pharmacy and gift shop

We need a letterhead, business card, gift voucher and possibly compliments slip design for our pharmacy and gift shop using our new logo.
The letterhead would need to be produced in both colour (purple and green) and grayscale and the business card would preferably be one-sided, but can be two-sided if this works better with the information it needs to have on it.

We would like a simple and elegant design, but not so simple that it looks like we've done it ourselves on Word. Use of our colours would be great but the letterhead would need to look good if printed on our black and white laser printer. If this is not possible then an additional version for grayscale would be needed.

We would need to receive high quality files that we can work with easily, such as pdf's for the letterhead that we can print instantly or order online as it appears on screen and business cards in jpeg and pdf so we can upload to printing sites.
We would like the vouchers in denominations of £5 and £10 in A5 size in a printable format such as PDF so that we don't have to resize.

Letterhead is for use in correspondence and invoicing to patients, surgeries, traders, customers etc.

Our preferred font is Orkney

Letterhead Info
Address
47 Fenwick Rd.
Thornbeck
Westdale
CA17 4TW

Tel: (01846) 357148
Fax: (01846) 364057
Website: www.brackenfieldpharmacy.com
Email: patientcare@brackenfieldpharmacy.com

Business Card Info.
As above but email address is: rtkdenholm@postbox-mail.co.uk

Voucher Info.
Small print to state that any change will be paid as a credit note.
Space for a staff member to sign, date and stamp voucher

I have quite a few logo files so please ask if you need more uploaded. Or if you need more information to improve the design then please contact me.

Target Market(s)

Both retail customers and professional colleagues

Industry/Entity Type

Pharmacy

Font styles to use
Other font styles liked:
• orkney

Colors
ffffff
9bcb3c
6b449b

Requirements
Must have
• Must be clear and legible with a professional feel. Must use the logo well and all aspects of the designs should work well together.
• Final files MUST be easy to use for non-computer specialists. I need staff to be able to pull up a letterhead template easily if they are writing a letter or raising an invoice. The business card must be in a format ready to be sent to print.
Nice to have
• Letterhead available in a word processor program like word so that letters can be sent by email as well as print or print and scan.

```html
<!DOCTYPE html>
<html lang="en">
<head>
<meta charset="utf-8">
<title>Brackenfield Pharmacy – Business Card</title>
<link rel="stylesheet" href="https://fonts.googleapis.com/css2?family=Poppins:wght@400;500;600;700&display=swap">
<style>
  :root {
    --purple: #6b449b;
    --purple-deep: #5a3186;
    --green: #9bcb3c;
    --white: #ffffff;
    --ink: #2b2b2b;
    --backdrop: #ebebeb;
  }
  * { margin: 0; padding: 0; box-sizing: border-box; }
  html, body { width: 1200px; height: 800px; overflow: hidden; }
  body {
    background: var(--backdrop);
    font-family: "Poppins", sans-serif;
    display: flex;
    align-items: center;
    justify-content: center;
    gap: 60px;
  }
  .card {
    width: 510px;
    height: 292px;
    position: relative;
    overflow: hidden;
    box-shadow: 0 6px 20px rgba(0,0,0,0.08);
  }
  /* Front */
  .card-front { background: var(--white); }
  .brand {
    position: absolute;
    display: flex;
    align-items: center;
    gap: 10px;
    font-weight: 500;
    letter-spacing: 0.06em;
    text-transform: uppercase;
    white-space: nowrap;
  }
  .card-front .brand { top: 34px; left: 34px; color: var(--purple); font-size: 17px; }
  .brand-square { width: 22px; height: 22px; background: var(--purple); flex: none; }
  .person { position: absolute; top: 104px; left: 34px; color: var(--ink); }
  .person-name {
    color: var(--purple);
    font-weight: 700;
    font-size: 15px;
    letter-spacing: 0.08em;
    text-transform: uppercase;
  }
  .person-role {
    font-size: 8px;
    letter-spacing: 0.1em;
    text-transform: uppercase;
    margin-bottom: 8px;
  }
  .person-address { font-size: 9.5px; line-height: 1.45; font-style: normal; }
  .contact {
    position: absolute;
    right: 30px;
    bottom: 38px;
    padding-left: 12px;
    border-left: 2px solid var(--green);
    font-size: 10px;
    line-height: 1.5;
    color: var(--ink);
    list-style: none;
    white-space: nowrap;
  }
  .edge-band { position: absolute; bottom: 0; height: 8px; }
  .edge-band-purple { left: 0; width: 62%; height: 5px; bottom: 3px; background: var(--purple); }
  .edge-band-green { right: 0; width: 38%; background: var(--green); }
  /* Back */
  .card-back {
    background: var(--purple-deep);
    display: flex;
    align-items: center;
    justify-content: center;
  }
  .card-back .brand { position: static; color: var(--white); font-size: 22px; }
  .card-back .brand-square { width: 28px; height: 28px; background: var(--white); }
</style>
</head>
<body>
  <section class="card card-front" aria-label="Business card front">
    <div class="brand"><span class="brand-square"></span>Brackenfield Pharmacy</div>
    <div class="person">
      <p class="person-name">Ruth Denholm</p>
      <p class="person-role">President</p>
      <address class="person-address">47 Fenwick Rd. Thornbeck<br>Westdale CA17 4TW</address>
    </div>
    <ul class="contact">
      <li>t: (01846) 357148</li>
      <li>f: (01846) 364057</li>
      <li>rtkdenholm@postbox-mail.co.uk</li>
      <li>www.brackenfieldpharmacy.com</li>
    </ul>
    <div class="edge-band edge-band-purple"></div>
    <div class="edge-band edge-band-green"></div>
  </section>

  <section class="card card-back" aria-label="Business card back">
    <div class="brand"><span class="brand-square"></span>Brackenfield Pharmacy</div>
  </section>
</body>
</html>
```